Design 4 pages for an event discovery website

This is a contest for the design of 4 pages for an events discovery website. The feature is part of the new sign-up process.

Please see the attached document for a full scope, mockups and the parent category icons.

Target Market(s)

18-35 Australian event goers

Industry/Entity Type

Events

Number of Pages Required

4 page

```html
<!DOCTYPE html>
<html lang="en">
<head>
<meta charset="utf-8">
<title>Lumora – Sign up, step 1 of 5</title>
<link rel="stylesheet" href="https://fonts.googleapis.com/css2?family=Open+Sans:wght@400;600;700&display=swap">
<style>
  :root {
    --ink: #ffffff;
    --ink-soft: #e9e9e9;
    --alert: #ff4a5c;
    --blue-top: #2a7fc4;
    --blue-bottom: #145b98;
    --blue-divider: #8fc3ee;
    --search-blue: #0a72cf;
    --green: #2fb24f;
    --footer: #2b2b2b;
    --rule: rgba(255,255,255,0.55);
    --scene-a: #2a0f1c;
    --scene-b: #3a1426;
    --scene-c: #120a12;
  }
  * { box-sizing: border-box; margin: 0; padding: 0; }
  html, body { width: 1200px; height: 795px; overflow: hidden; }
  body { font-family: "Open Sans", Arial, sans-serif; color: var(--ink); background: var(--scene-c); }

  .page { position: relative; width: 1200px; height: 795px; overflow: hidden; }

  .backdrop {
    position: absolute; inset: 0 0 91px 0;
    background:
      radial-gradient(ellipse at 72% 45%, var(--scene-b) 0%, transparent 55%),
      radial-gradient(ellipse at 20% 60%, #2b1020 0%, transparent 50%),
      linear-gradient(180deg, var(--scene-c) 0%, var(--scene-a) 60%, #1b0b14 100%);
  }

  .site-header {
    position: absolute; left: 0; top: 0; width: 1200px; height: 94px;
    border-bottom: 1px solid var(--rule);
  }
  .brand { position: absolute; left: 60px; top: 28px; }
  .brand-name { font-size: 27px; font-weight: 400; letter-spacing: 1px; line-height: 32px; }
  .brand-tag { font-size: 14px; line-height: 18px; }

  .search {
    position: absolute; left: 688px; top: 28px; width: 211px; height: 39px;
    background: var(--search-blue); border-radius: 2px;
    display: flex; align-items: center; padding: 0 12px 0 19px;
    font-size: 13px; justify-content: space-between;
  }
  .btn-green {
    position: absolute; top: 28px; height: 40px; width: 107px;
    background: var(--green); border-radius: 2px;
    font-size: 17px; font-weight: 600; text-align: center; line-height: 40px;
  }
  .btn-signup { left: 912px; }
  .btn-login { left: 1033px; }

  .intro { position: absolute; left: 114px; top: 136px; }
  .step-title { font-size: 23px; font-weight: 700; line-height: 32px; margin-bottom: 10px; }
  .intro p { font-size: 15.5px; line-height: 29px; color: var(--ink-soft); }

  .connect-list { position: absolute; left: 116px; top: 307px; list-style: none; }
  .connect-row { position: relative; height: 58px; margin-bottom: 22px; }
  .connect-btn {
    display: flex; width: 332px; height: 58px; border-radius: 3px; overflow: hidden;
    background: linear-gradient(180deg, var(--blue-top), var(--blue-bottom));
  }
  .connect-icon {
    width: 100px; display: flex; align-items: center; justify-content: center;
    border-right: 3px solid var(--blue-divider);
  }
  .connect-label {
    flex: 1; display: flex; align-items: center; justify-content: center;
    font-size: 16px; font-weight: 700; letter-spacing: 0.3px;
  }
  .connect-status {
    position: absolute; left: 356px; top: 0; font-size: 14px; line-height: 24px; color: var(--alert);
  }

  .site-footer {
    position: absolute; left: 0; bottom: 0; width: 1200px; height: 91px;
    background: var(--footer); text-align: center;
  }
  .social { display: flex; justify-content: center; gap: 6px; padding-top: 22px; }
  .social span { width: 21px; height: 21px; background: var(--ink); border-radius: 3px; }
  .copyright { font-size: 12px; font-weight: 600; margin-top: 9px; }
  .page-code { position: absolute; right: 23px; top: 40px; font-size: 13px; }
</style>
</head>
<body>
<div class="page">
  <div class="backdrop" role="img" aria-label="Photo of young people celebrating at a party with confetti, darkened"></div>

  <header class="site-header">
    <div class="brand">
      <div class="brand-name">LUMORA</div>
      <div class="brand-tag">Find Events</div>
    </div>
    <div class="search">
      <span>Search</span>
      <svg width="16" height="16" viewBox="0 0 16 16" aria-hidden="true">
        <circle cx="6.5" cy="6.5" r="4.6" fill="none" stroke="#fff" stroke-width="2.2"/>
        <line x1="10" y1="10" x2="14.5" y2="14.5" stroke="#fff" stroke-width="2.6" stroke-linecap="round"/>
      </svg>
    </div>
    <div class="btn-green btn-signup">SIGN UP</div>
    <div class="btn-green btn-login">LOGIN</div>
  </header>

  <section class="intro">
    <h1 class="step-title">STEP 1 OF 5</h1>
    <p>Link in all your other social media accounts and music players</p>
    <p>By linking your accounts, We can save you a lot of time</p>
    <p>By automatically determining your interests</p>
  </section>

  <ul class="connect-list">
    <li class="connect-row">
      <div class="connect-btn">
        <div class="connect-icon"><svg width="22" height="22" aria-hidden="true"><circle cx="11" cy="11" r="10" fill="#fff"/></svg></div>
        <div class="connect-label">CHIRPER</div>
      </div>
      <div class="connect-status">Linked</div>
    </li>
    <li class="connect-row">
      <div class="connect-btn">
        <div class="connect-icon"><svg width="22" height="22" aria-hidden="true"><rect x="1" y="1" width="20" height="20" rx="3" fill="#fff"/></svg></div>
        <div class="connect-label">SNAPGRAM</div>
      </div>
    </li>
    <li class="connect-row">
      <div class="connect-btn">
        <div class="connect-icon"><svg width="22" height="22" aria-hidden="true"><circle cx="11" cy="11" r="10" fill="#fff"/></svg></div>
        <div class="connect-label">TUNELY</div>
      </div>
      <div class="connect-status">We don’t have that features yet<br>but have requested your interest</div>
    </li>
    <li class="connect-row">
      <div class="connect-btn">
        <div class="connect-icon"><svg width="22" height="22" aria-hidden="true"><rect x="1" y="1" width="20" height="20" rx="3" fill="#fff"/></svg></div>
        <div class="connect-label">SONGSHOP</div>
      </div>
    </li>
  </ul>

  <footer class="site-footer">
    <div class="social" aria-label="Social links">
      <span></span><span></span><span></span><span></span><span></span>
    </div>
    <div class="copyright">Copyright © 2015 lumora. All Rights Reserved.</div>
    <div class="page-code">c14</div>
  </footer>
</div>
</body>
</html>
```